Flyer for Professional Advisers - 2 versions one for fax one for email

Please design a flyer for our company Quillford Advisory. The flyer is aimed at professional advisers such as accountants / financial planners for a marketing campaign we are running. A word doc is attached with the text for the flyer. It is important that all of this content is included in the flyer.

We are running the marketing campaign through both email and fax so will need two versions of the flyer:

1. Lower resolution MS Word document (editable) template that is suitable for faxing - ie black and white, and

2. MS Office email template (MS office 20101 compatible) that has more detailed graphics and colours (or background images etc) but still gets the basic message accross in plain text if possible if the recipient email client blocks image files.

In addition to the text/content i have attached our company logo. Please refer to our website www.quillfordadvisory.com.au for an indication of our preferred colours / style.

Project Deadline Extended
Reason: Due to other urgent matters management have not had a chance to look at designs in original timeframe

Industry/Entity Type

Financial

```html
<!DOCTYPE html>
<html lang="en">
<head>
<meta charset="utf-8">
<title>Quillford Advisory – Referral Flyer (Email and Fax)</title>
<link rel="stylesheet" href="https://fonts.googleapis.com/css2?family=PT+Sans:wght@400;700&family=PT+Sans+Narrow:wght@700&family=Roboto+Condensed:wght@400;700&display=swap">
<style>
:root{
  --board:#5a3f2e;
  --label:#f3ece4;
  --email-bg:#3e4336;
  --email-lime:#8dc63f;
  --email-green:#3daa4a;
  --email-orange:#df9b27;
  --email-text:#f1f1ea;
  --fax-bg:#ffffff;
  --fax-mid:#8a8a8a;
  --fax-text:#222222;
  --white:#ffffff;
}
*{box-sizing:border-box;margin:0;padding:0}
html,body{width:1200px;height:864px;overflow:hidden}
body{background:var(--board);font-family:"PT Sans",sans-serif;position:relative}
.board-label{position:absolute;top:46px;color:var(--label);font-family:"PT Sans",sans-serif;font-size:19px;letter-spacing:.3px}
.flyer{position:absolute;top:88px;width:518px;height:728px;overflow:hidden;box-shadow:3px 4px 10px rgba(0,0,0,.45)}
.flyer--email{left:67px;background:var(--email-bg);color:var(--email-text)}
.flyer--fax{left:619px;background:var(--fax-bg);color:var(--fax-text)}
.flyer > *{position:absolute}
.header-art,.bubble-art{left:0;top:0}
.brand{left:29px;top:24px;font-family:"PT Sans",sans-serif;font-weight:700;font-size:36px;letter-spacing:.5px;line-height:1}
.flyer--email .brand{color:#3a3d35}
.flyer--fax .brand{color:var(--white)}
.headline{left:29px;top:98px;font-family:"PT Sans Narrow",sans-serif;font-weight:700;font-size:28px;line-height:34px;letter-spacing:1.2px;color:var(--white);text-shadow:1px 2px 3px rgba(0,0,0,.45)}
.intro{text-align:center;font-size:8.4px;line-height:11.5px}
.intro h2{font-family:"PT Sans",sans-serif;font-weight:700;font-size:14.5px;line-height:19px;margin-bottom:7px}
.flyer--email .intro h2{color:var(--email-lime)}
.flyer--fax .intro h2{color:var(--fax-text)}
.intro--banks{left:326px;top:196px;width:160px}
.intro--smart{left:24px;top:240px;width:250px}
.step{text-align:center;color:var(--white);font-size:8.2px;line-height:10.5px;text-transform:uppercase;white-space:nowrap}
.step h3{font-family:"PT Sans Narrow",sans-serif;font-size:18px;line-height:20px;letter-spacing:.6px;margin-bottom:3px;text-shadow:1px 1px 2px rgba(0,0,0,.4)}
.step--identify{left:26px;top:364px;width:164px;transform:rotate(-3deg)}
.step--refer{left:190px;top:366px;width:140px;transform:rotate(-5deg)}
.step--earn{left:350px;top:366px;width:140px;transform:rotate(13deg)}
.why{left:29px;top:490px;width:248px;font-size:8.4px;line-height:11px;text-align:justify}
.why h2{font-family:"PT Sans",sans-serif;font-weight:400;font-size:14.5px;line-height:18px;margin-bottom:2px;text-align:left}
.flyer--email .why h2{color:var(--email-lime)}
.photo{left:293px;top:483px}
.cta{left:29px;top:610px;font-family:"Roboto Condensed",sans-serif;font-weight:700;font-size:13.5px;line-height:17.5px}
.flyer--email .cta{color:var(--email-lime)}
.address{left:29px;top:674px;font-size:9.5px;line-height:12.5px;font-weight:700}
.licence{left:29px;top:700px;font-size:8.4px}
.contact{right:32px;top:648px;text-align:right;font-family:"Roboto Condensed",sans-serif}
.contact__phone{font-size:18.5px;line-height:22px}
.contact__phone strong{letter-spacing:1.2px;font-weight:700}
.contact__web{font-size:15px;font-weight:700;letter-spacing:.9px;line-height:24px}
.contact__email{font-family:"PT Sans",sans-serif;font-weight:700;font-size:9.5px;margin-top:4px}
</style>
</head>
<body>

<p class="board-label" style="left:67px">email template</p>
<p class="board-label" style="left:617px">for Fax</p>

<!-- Email version -->
<section class="flyer flyer--email">
  <svg class="header-art" width="518" height="240" viewBox="0 0 518 240" aria-hidden="true">
    <defs>
      <linearGradient id="emailHeader" x1="0" y1="0" x2="0" y2="1">
        <stop offset="0" stop-color="#9bd14a"/>
        <stop offset="1" stop-color="#73b22e"/>
      </linearGradient>
    </defs>
    <path d="M0 0H518V150C430 205 300 195 190 170C110 152 45 150 0 162Z" fill="url(#emailHeader)"/>
    <path d="M0 162C45 150 110 152 190 170C300 195 430 205 518 150V162C430 215 300 210 190 184C110 166 45 166 0 176Z" fill="#2e3328"/>
    <path d="M0 150C90 135 200 160 300 178C400 195 470 180 518 150" stroke="#c4e88a" stroke-width="1.5" fill="none" opacity=".6"/>
  </svg>
  <p class="brand">QUILLFORD ADVISORY</p>
  <h1 class="headline">MORTGAGE REFERRAL SOLUTIONS<br>FOR PROFESSIONAL ADVISERS</h1>

  <div class="intro intro--banks">
    <h2>Are you referring<br>clients to local banks and<br>not generating revenue?</h2>
    <p>Quillford Advisory is one of Australia's leading providers of referral based mortgage solutions. We provide business professionals with access to one of the most time and cost effective mortgage services available in Australia.</p>
  </div>
  <div class="intro intro--smart">
    <h2>Are you looking for a smart alternative<br>to mortgage broker referrals?</h2>
    <p>Unlike a mortgage broking service, we pass the majority of revenue to the client owner and we ensure that you control the client referral process.</p>
  </div>

  <svg class="bubble-art" width="518" height="728" viewBox="0 0 518 728" aria-hidden="true">
    <ellipse cx="108" cy="403" rx="88" ry="53" fill="var(--email-green)" stroke="#e8f5d8" stroke-width="1.5"/>
    <path d="M140 448L165 478L160 440Z" fill="var(--email-green)"/>
    <ellipse cx="260" cy="402" rx="82" ry="52" fill="var(--email-orange)" stroke="#fbe6c0" stroke-width="1.5"/>
    <path d="M300 440L335 470L318 432Z" fill="var(--email-orange)"/>
    <ellipse cx="418" cy="408" rx="88" ry="54" fill="var(--email-lime)" stroke="#eaf6d8" stroke-width="1.5" transform="rotate(10 418 408)"/>
    <path d="M350 440L340 470L372 450Z" fill="var(--email-lime)"/>
  </svg>
  <div class="step step--identify"><h3>IDENTIFY</h3>Identify client mortgage<br>requirements for new<br>borrowings or refinance of<br>existing facilities</div>
  <div class="step step--refer"><h3>REFER</h3>Use our market leading<br>software to refer your<br>clients to preferred<br>lenders across Australia</div>
  <div class="step step--earn"><h3>EARN</h3>Receive generous<br>commission payments in the<br>month following<br>settlement and build<br>ongoing revenue</div>

  <div class="why">
    <h2>WHY QUILLFORD ADVISORY</h2>
    <p>Quillford Advisory is an industry leader in providing mortgage referral solutions for both licensed and unlicensed referrers. Our unique model dispels the misconception that professionals must either hold a credit licence or deal with a mortgage broker in order to manage the debt requirements of their clients.</p>
  </div>

  <svg class="photo" width="210" height="140" viewBox="0 0 210 140" role="img" aria-label="Photo of a smiling group of professionals">
    <defs>
      <radialGradient id="emailPhoto" cx=".5" cy=".45" r=".6">
        <stop offset="0" stop-color="#e4c8ae"/>
        <stop offset="1" stop-color="#8e7564"/>
      </radialGradient>
    </defs>
    <ellipse cx="102" cy="64" rx="100" ry="60" fill="url(#emailPhoto)" stroke="#f2f2ea" stroke-width="2"/>
    <path d="M155 110L178 138L168 104Z" fill="#f2f2ea"/>
  </svg>

  <p class="cta">Call us today or visit our website &nbsp;to find<br>Out more about our service</p>
  <p class="address">Quillford Advisory Level 12/88<br>Harbour Lane Melbourne VIC 3000</p>
  <p class="licence">Australian Credit Licence 400912</p>
  <div class="contact">
    <p class="contact__phone">CONTACT US: <strong>1300 555 018</strong></p>
    <p class="contact__web">www.quillfordadvisory.com.au</p>
    <p class="contact__email">Email: info@quillfordadvisory.com.au</p>
  </div>
</section>

<!-- Fax version -->
<section class="flyer flyer--fax">
  <svg class="header-art" width="518" height="240" viewBox="0 0 518 240" aria-hidden="true">
    <defs>
      <linearGradient id="faxHeader" x1="0" y1="0" x2="0" y2="1">
        <stop offset="0" stop-color="#3c3c3c"/>
        <stop offset="1" stop-color="#4e4e4e"/>
      </linearGradient>
      <linearGradient id="faxFade" x1="0" y1="0" x2="0" y2="1">
        <stop offset="0" stop-color="#9a9a9a"/>
        <stop offset="1" stop-color="#ffffff"/>
      </linearGradient>
    </defs>
    <path d="M0 0H518V150C430 205 300 195 190 170C110 152 45 150 0 162Z" fill="url(#faxHeader)"/>
    <path d="M0 162C45 150 110 152 190 170C300 195 430 205 518 150V200C430 235 300 225 190 205C110 190 45 190 0 200Z" fill="url(#faxFade)"/>
  </svg>
  <p class="brand">QUILLFORD ADVISORY</p>
  <h1 class="headline">MORTGAGE REFERRAL SOLUTIONS<br>FOR PROFESSIONAL ADVISERS</h1>

  <div class="intro intro--banks">
    <h2>Are you referring<br>clients to local banks and<br>not generating revenue?</h2>
    <p>Quillford Advisory is one of Australia's leading providers of referral based mortgage solutions. We provide business professionals with access to one of the most time and cost effective mortgage services available in Australia.</p>
  </div>
  <div class="intro intro--smart">
    <h2>Are you looking for a smart alternative<br>to mortgage broker referrals?</h2>
    <p>Unlike a mortgage broking service, we pass the majority of revenue to the client owner and we ensure that you control the client referral process.</p>
  </div>

  <svg class="bubble-art" width="518" height="728" viewBox="0 0 518 728" aria-hidden="true">
    <ellipse cx="108" cy="403" rx="88" ry="53" fill="#5a5a5a" stroke="#ffffff" stroke-width="1.5"/>
    <path d="M140 448L165 478L160 440Z" fill="#5a5a5a"/>
    <ellipse cx="260" cy="402" rx="82" ry="52" fill="var(--fax-mid)" stroke="#ffffff" stroke-width="1.5"/>
    <path d="M300 440L335 470L318 432Z" fill="var(--fax-mid)"/>
    <ellipse cx="418" cy="408" rx="88" ry="54" fill="#4a4a4a" stroke="#ffffff" stroke-width="1.5" transform="rotate(10 418 408)"/>
    <path d="M350 440L340 470L372 450Z" fill="#4a4a4a"/>
  </svg>
  <div class="step step--identify"><h3>IDENTIFY</h3>Identify client mortgage<br>requirements for new<br>borrowings or refinance of<br>existing facilities</div>
  <div class="step step--refer"><h3>REFER</h3>Use our market leading<br>software to refer your<br>clients to preferred<br>lenders across Australia</div>
  <div class="step step--earn"><h3>EARN</h3>Receive generous<br>commission payments in the<br>month following<br>settlement and build<br>ongoing revenue</div>

  <div class="why">
    <h2>WHY QUILLFORD ADVISORY</h2>
    <p>Quillford Advisory is an industry leader in providing mortgage referral solutions for both licensed and unlicensed referrers. Our unique model dispels the misconception that professionals must either hold a credit licence or deal with a mortgage broker in order to manage the debt requirements of their clients.</p>
  </div>

  <svg class="photo" width="210" height="140" viewBox="0 0 210 140" role="img" aria-label="Black and white photo of a smiling group of professionals">
    <defs>
      <radialGradient id="faxPhoto" cx=".5" cy=".45" r=".6">
        <stop offset="0" stop-color="#d6d6d6"/>
        <stop offset="1" stop-color="#6e6e6e"/>
      </radialGradient>
    </defs>
    <ellipse cx="102" cy="64" rx="100" ry="60" fill="url(#faxPhoto)" stroke="#ffffff" stroke-width="2"/>
  </svg>

  <p class="cta">Call us today or visit our website &nbsp;to find<br>Out more about our service</p>
  <p class="address">Quillford Advisory Level 12/88<br>Harbour Lane Melbourne VIC 3000</p>
  <p class="licence">Australian Credit Licence 400912</p>
  <div class="contact">
    <p class="contact__phone">CONTACT US: <strong>1300 555 018</strong></p>
    <p class="contact__web">www.quillfordadvisory.com.au</p>
    <p class="contact__email">Email: info@quillfordadvisory.com.au</p>
  </div>
</section>

</body>
</html>
```